Business card

would like a double sided business card made up with my logos provided.
Prefer card to have black background and to use the black logos, with matching blue writing for the text.
One side to just be the logo, (Try to use both the black logos)
the other side to have the logo and also my credentials/business information.

Covering all aspects of Carpentry and Building Services

Marcus Thelwin
Qualified Carpenter
Mob: 0417263985
Email: rkt.joinery@fernmail.example
ABN: 47 619 283 504

Industry/Entity Type

Business

Contact Information for Business Card

Marcus Thelwin
Qualified Carpenter
Mob: 0417263985
ABN: 47 619 283 504

Requirements
Must have
• Please try to use both the black logos and incorporate into the card.

```html
<!DOCTYPE html>
<html lang="en">
<head>
<meta charset="utf-8">
<title>RKT Joinery – Business Card</title>
<link rel="stylesheet" href="https://fonts.googleapis.com/css2?family=Source+Sans+3:wght@400;600;700&display=swap">
<style>
  :root {
    --card-black: #0f1112;
    --edge-black: #000000;
    --paper: #ffffff;
    --cyan: #00e6f0;
    --blue: #2e7cf3;
    --logo-white: #ffffff;
    --logo-blue: #2f86f6;
  }
  * { margin: 0; padding: 0; box-sizing: border-box; }
  html, body {
    width: 1025px; height: 1200px; overflow: hidden;
    background: var(--paper);
    font-family: "Source Sans 3", "Myriad Pro", sans-serif;
  }
  .sheet { position: relative; width: 1025px; height: 1200px; }
  .card {
    position: absolute; left: 0; width: 1025px;
    background: var(--card-black);
    border: 4px solid var(--edge-black);
  }
  .card--front { top: 0; height: 586px; }
  .card--back { top: 614px; height: 586px; }

  .card__text { position: absolute; white-space: nowrap; line-height: 1; }
  .holder-name { left: 56px; top: 110px; font-size: 47px; font-weight: 700; color: var(--cyan); }
  .holder-role { left: 56px; top: 205px; font-size: 43px; font-weight: 400; color: var(--cyan); }
  .services {
    left: 0; right: 0; top: 298px; text-align: center;
    font-size: 39px; font-weight: 700; color: var(--blue); line-height: 54px;
    padding-left: 52px;
  }
  .contact-email { left: 0; right: 0; top: 440px; text-align: center; font-size: 44px; color: var(--blue); padding-left: 6px; }
  .contact-mobile { left: 56px; top: 502px; font-size: 44px; color: var(--blue); }
  .contact-abn { left: 576px; top: 502px; font-size: 44px; color: var(--blue); }
  .value { color: var(--cyan); }

  .brand { position: absolute; display: flex; align-items: center; gap: 12px; white-space: nowrap; }
  .brand__mark { display: block; background: var(--logo-blue); }
  .brand__name { font-weight: 600; color: var(--logo-white); letter-spacing: 2px; line-height: 1; }
  .brand--small { left: 760px; top: 96px; }
  .brand--small .brand__mark { width: 26px; height: 26px; }
  .brand--small .brand__name { font-size: 34px; }
  .brand--large { left: 0; right: 0; top: 238px; justify-content: center; gap: 22px; }
  .brand--large .brand__mark { width: 60px; height: 60px; }
  .brand--large .brand__name { font-size: 88px; letter-spacing: 4px; }
</style>
</head>
<body>
<main class="sheet">
  <section class="card card--front" aria-label="Card front">
    <div class="brand brand--small">
      <span class="brand__mark"></span>
      <span class="brand__name">RKT JOINERY</span>
    </div>
    <h1 class="card__text holder-name">Marcus Thelwin</h1>
    <p class="card__text holder-role">Qualified Carpenter</p>
    <p class="card__text services">Covering all aspects of Carpentry<br>and Building Services</p>
    <p class="card__text contact-email">Email: <span class="value">rkt.joinery@fernmail.example</span></p>
    <p class="card__text contact-mobile">Mobile: <span class="value">0417263985</span></p>
    <p class="card__text contact-abn">ABN: <span class="value">47 619 283 504</span></p>
  </section>

  <section class="card card--back" aria-label="Card back">
    <div class="brand brand--large">
      <span class="brand__mark"></span>
      <span class="brand__name">RKT JOINERY</span>
    </div>
  </section>
</main>
</body>
</html>
```